I have a tallow based business and I want to streamline my products

I have roughly 10 items that I would like to make lebals for in order to streamline my business, I am attaching the current design and am willing to work with this but would also like to see if you come up with something different, my biggest seller is my facewash , my webpage is themeadowlyco,com my current designs are below- The newest one is the light brown version which I do like but I am not sure how that will integrate or be streamlined with the remaining products, If you believe it can look similar and still be attractive, I am ok with that too,

My current Label Project Needs:

Tallow + Magnesium Lotion biodegradable wheat bottle
Tallow Cream Face Wash - biodegradable what bottle
Tallow Body Butter 8 oz jar with bamboo lid
Tallow Deodorant will be printed on a Kraft Paper tube
Tallow Face Cream for Day wear 2 oz glass jar with bamboo lid
Vitamin C Serum 2 oz serum bottle with bamboo pump
Blue Algae Toner 4 oz glass bottle
Tallow + Hyaluronic 2oz face cream jar
'
My project is to display sustainable products, eco friendly packaging, organic , natural and holistic

I am ok with the newest label I attached but I am also ok with a minimalistic project, I would love to choose from a couple of designs.

Thank you so much

```html
<!DOCTYPE html>
<html lang="en">
<head>
<meta charset="utf-8">
<title>Label Set – Toner, Vitamin C Serum, Face Cream</title>
<link rel="stylesheet" href="https://fonts.googleapis.com/css2?family=Jost:wght@400;500;600;700&family=Roboto+Condensed:wght@400;700&family=Source+Sans+3:wght@400&display=swap">
<style>
  :root {
    --paper: #efe6d8;
    --ink: #4a3636;
    --bleed: #e8353a;
    --safe: #29abe2;
    --rule: #111111;
    --photo-light: #c9b8a6;
    --photo-dark: #7d6757;
  }
  * { box-sizing: border-box; margin: 0; padding: 0; }
  html, body { width: 1034px; height: 1200px; overflow: hidden; background: #ffffff; }
  body { position: relative; font-family: "Jost", sans-serif; color: var(--ink); }

  .abs { position: absolute; }
  .centered { transform: translate(-50%, -50%); white-space: nowrap; text-align: center; }

  .section-title { font-family: "Source Sans 3", sans-serif; font-size: 20px; color: var(--rule); left: 97px; transform: translateY(-50%); }
  .dim-label { font-family: "Source Sans 3", sans-serif; font-size: 14px; color: var(--rule); }
  .dim-label.vertical { transform: translate(-50%, -50%) rotate(-90deg); }

  .bleed-box { border: 1px solid var(--bleed); background: var(--paper); }
  .safe-box { border: 1.5px solid var(--safe); }

  .brand-band { background: var(--ink); color: #ffffff; font-family: "Jost", sans-serif; font-weight: 500; font-size: 13px; letter-spacing: 0.2px; display: flex; align-items: flex-end; justify-content: center; padding-bottom: 8px; }

  .badge-icon { width: 40px; height: 40px; transform: translate(-50%, -50%); }
  .badge-placeholder { width: 30px; height: 30px; border-radius: 6px; transform: translate(-50%, -50%); background: linear-gradient(160deg, var(--photo-light), var(--photo-dark)); }
  .badge-label { font-size: 8.5px; line-height: 10px; font-weight: 500; letter-spacing: 0.2px; }

  .maker { font-size: 10px; line-height: 13.3px; letter-spacing: 0.3px; white-space: nowrap; }
  .maker strong { font-weight: 700; letter-spacing: 0.4px; }

  .product-sub { font-weight: 700; font-size: 16px; letter-spacing: 1px; }
  .product-name { font-weight: 700; line-height: 0.95; letter-spacing: 0.3px; }
  .net-weight { font-weight: 700; font-size: 11px; letter-spacing: 0.4px; word-spacing: 2px; }

  .ingredients { font-family: "Roboto Condensed", sans-serif; text-align: justify; }
  .ingredients strong { font-weight: 700; }

  .rotated { transform: translate(-50%, -50%) rotate(-90deg); }
  .photo-slot { background: linear-gradient(170deg, var(--photo-light), var(--photo-dark)); border-radius: 6px; }
</style>
</head>
<body>

<svg width="0" height="0" style="position:absolute">
  <defs>
    <symbol id="icon-leaf" viewBox="0 0 40 40">
      <circle cx="20" cy="20" r="16" fill="none" stroke="#4a3636" stroke-width="1.6"/>
      <path d="M12 27 C13 17 20 12 28 12 C28 21 22 27 13 27 Z" fill="none" stroke="#4a3636" stroke-width="1.6"/>
      <path d="M12 28 L24 16" stroke="#4a3636" stroke-width="1.4"/>
    </symbol>
    <symbol id="icon-hand-heart" viewBox="0 0 40 40">
      <path d="M14 30 L26 18 M17 12 L27 22 M21 9 L31 19 M24 8 L33 17" stroke="#4a3636" stroke-width="1.6" stroke-linecap="round" fill="none"/>
      <path d="M20 31 C20 23 28 20 32 14" stroke="#4a3636" stroke-width="1.6" fill="none" stroke-linecap="round"/>
      <path d="M13 34 C4 28 4 21 8.5 20 C11 19.5 12.5 21 13 22.5 C13.5 21 15 19.5 17.5 20 C22 21 22 28 13 34 Z" fill="#4a3636"/>
    </symbol>
    <symbol id="icon-handshake" viewBox="0 0 40 40">
      <path d="M3 13 L10 8 L14 14 L7 19 Z M37 13 L30 8 L26 14 L33 19 Z" fill="#4a3636"/>
      <path d="M12 12 L20 10 L28 13 L31 19 L22 29 L17 31 L9 22 Z" fill="none" stroke="#4a3636" stroke-width="1.6" stroke-linejoin="round"/>
      <path d="M20 10 L15 16 C17 18 19 17 22 14 M15 23 L18 26 M18 21 L21 24 M21 19 L24 22" stroke="#4a3636" stroke-width="1.5" fill="none" stroke-linecap="round"/>
    </symbol>
  </defs>
</svg>

<!-- Dimension rules -->
<svg class="abs" style="left:0;top:0" width="1034" height="1200" aria-hidden="true">
  <g stroke="#111" stroke-width="1.6" fill="#111">
    <line x1="258" y1="106" x2="784" y2="106"/>
    <line x1="256" y1="100" x2="256" y2="112"/><line x1="786" y1="100" x2="786" y2="112"/>
    <polygon points="258,106 268,102 268,110" stroke="none"/><polygon points="784,106 774,102 774,110" stroke="none"/>
    <line x1="220" y1="138" x2="220" y2="400"/>
    <line x1="214" y1="136" x2="222" y2="136"/><line x1="214" y1="402" x2="222" y2="402"/>
    <polygon points="220,138 216,148 224,148" stroke="none"/><polygon points="220,400 216,390 224,390" stroke="none"/>

    <line x1="324" y1="503" x2="718" y2="503"/>
    <line x1="322" y1="497" x2="322" y2="509"/><line x1="720" y1="497" x2="720" y2="509"/>
    <polygon points="324,503 334,499 334,507" stroke="none"/><polygon points="718,503 708,499 708,507" stroke="none"/>
    <line x1="284" y1="543" x2="284" y2="804"/>
    <line x1="278" y1="541" x2="286" y2="541"/><line x1="278" y1="806" x2="286" y2="806"/>
    <polygon points="284,543 280,553 288,553" stroke="none"/><polygon points="284,804 280,794 288,794" stroke="none"/>

    <line x1="126" y1="894" x2="915" y2="894"/>
    <line x1="124" y1="888" x2="124" y2="900"/><line x1="917" y1="888" x2="917" y2="900"/>
    <polygon points="126,894 136,890 136,898" stroke="none"/><polygon points="915,894 905,890 905,898" stroke="none"/>
    <line x1="81" y1="932" x2="81" y2="1126"/>
    <line x1="73" y1="930" x2="83" y2="930"/><line x1="73" y1="1128" x2="83" y2="1128"/>
    <polygon points="81,932 77,942 85,942" stroke="none"/><polygon points="81,1126 77,1116 85,1116" stroke="none"/>
  </g>
</svg>

<!-- ============ TONER ============ -->
<section class="label-toner">
  <h2 class="abs section-title" style="top:69px;font-weight:400">Toner</h2>
  <div class="abs dim-label centered" style="left:521px;top:86px">4 in</div>
  <div class="abs dim-label vertical" style="left:201px;top:268px">2 in</div>

  <div class="abs bleed-box" style="left:239px;top:120px;width:563px;height:298px"></div>
  <div class="abs safe-box" style="left:256px;top:136px;width:530px;height:266px"></div>
  <div class="abs brand-band" style="left:450px;top:121px;width:141px;height:48px">THE MEADOWLY CO.</div>

  <div class="abs badge-placeholder" style="left:302px;top:172px" role="img" aria-label="Small cow head icon"></div>
  <svg class="abs badge-icon" style="left:378px;top:173px"><use href="#icon-leaf"/></svg>
  <div class="abs badge-label centered" style="left:302px;top:207px">GRASS FED<br>TALLOW</div>
  <div class="abs badge-label centered" style="left:378px;top:207px">ORGANIC<br>INGREDIENTS</div>
  <svg class="abs badge-icon" style="left:302px;top:248px"><use href="#icon-hand-heart"/></svg>
  <svg class="abs badge-icon" style="left:378px;top:248px"><use href="#icon-handshake"/></svg>
  <div class="abs badge-label centered" style="left:302px;top:272px">HAND CRAFTED</div>
  <div class="abs badge-label centered" style="left:378px;top:272px">FAIR TRADE</div>

  <div class="abs maker" style="left:268px;top:320px">
    MANUFACTURED BY:<br><strong>LINDENVALE PURE ORGANICS</strong><br>PO. BOX 4471 ELMRIDGE,<br>VA 24019<br>themeadowlyco.com
  </div>

  <div class="abs product-sub centered" style="left:521px;top:235px">AQUA LUMINA</div>
  <div class="abs" style="left:445px;top:246px;width:151px;height:1.6px;background:var(--ink)"></div>
  <div class="abs product-name centered" style="left:521px;top:277px;font-size:25px">BLUE ALGAE<br>TONER</div>
  <div class="abs product-sub centered" style="left:521px;top:334px;font-size:14px;letter-spacing:0.6px">PROBIOTICS</div>
  <div class="abs net-weight centered" style="left:522px;top:379px">NET WT.&nbsp; 4 OZ / 250G</div>

  <div class="abs ingredients" style="left:630px;top:150px;width:142px;font-size:11.5px;line-height:15.5px">
    <strong style="font-size:15px;display:block;line-height:18px;margin-bottom:-1px">Ingredients:</strong>
    Lorem ipsum dolor sit amet, consectetuer adipiscing elit, sed diam nonummy nibh Lorem ipsum dolor sit amet, consectetuer adipiscing elit, sed diam nonummy nibh euismod tincidunt ut laoreet dolore magna aliquam erat volutpat. Ut wisi enim ad
  </div>
</section>

<!-- ============ VITAMIN C SERUM ============ -->
<section class="label-serum">
  <h2 class="abs section-title" style="top:486px;font-weight:400">Vit C Serum</h2>
  <div class="abs dim-label centered" style="left:521px;top:489px">3 in</div>
  <div class="abs dim-label vertical" style="left:265px;top:673px">2 in</div>

  <div class="abs bleed-box" style="left:306px;top:524px;width:430px;height:298px"></div>
  <div class="abs safe-box" style="left:322px;top:541px;width:398px;height:265px"></div>
  <div class="abs brand-band" style="left:450px;top:525px;width:141px;height:47px">THE MEADOWLY CO.</div>

  <div class="abs ingredients rotated" style="left:359px;top:673px;width:241px;height:58px;font-family:'Roboto Condensed',sans-serif;font-size:8px;line-height:8.3px">
    Lorem ipsum dolor sit amet, consectetuer adipiscing elit, sed diam nonummy nibh euismod tincidunt ut laoreet dolore magna aliquam erat volutpat. Ut wisi enim ad minim veniam, quis nostrud exerci tation ullamcorper suscipit lobortis nisl ut aliquip ex ea commodo consequat. Duis autem vel eum iriure dolor in hendrerit in vulputate velit
  </div>

  <div class="abs product-name centered" style="left:521px;top:676px;font-size:31px;line-height:32px">VITAMIN C<br>SERUM</div>
  <div class="abs net-weight centered" style="left:522px;top:786px">NET WT.&nbsp; 4 OZ / 250G</div>

  <div class="abs maker rotated" style="left:677px;top:722px;width:144px;height:64px;font-size:9.5px;line-height:13px">
    MANUFACTURED BY:<br><strong>LINDENVALE PURE ORGANICS</strong><br>PO. BOX 4471 ELMRIDGE,<br>VA 24019<br>themeadowlyco.com
  </div>
</section>

<!-- ============ FACE CREAM ============ -->
<section class="label-face-cream">
  <h2 class="abs section-title" style="top:855px;font-weight:400">Face Cream</h2>
  <div class="abs dim-label centered" style="left:521px;top:880px">6 in</div>
  <div class="abs dim-label vertical" style="left:61px;top:1029px">1,5 in</div>

  <div class="abs bleed-box" style="left:107px;top:914px;width:827px;height:230px"></div>
  <div class="abs safe-box" style="left:124px;top:930px;width:793px;height:198px"></div>
  <div class="abs brand-band" style="left:450px;top:914px;width:141px;height:47px">THE MEADOWLY CO.</div>

  <div class="abs badge-placeholder" style="left:175px;top:956px" role="img" aria-label="Small cow head icon"></div>
  <svg class="abs badge-icon" style="left:247px;top:956px"><use href="#icon-leaf"/></svg>
  <div class="abs badge-label centered" style="left:175px;top:988px">GRASS FED<br>TALLOW</div>
  <div class="abs badge-label centered" style="left:247px;top:988px">ORGANIC<br>INGREDIENTS</div>
  <svg class="abs badge-icon" style="left:175px;top:1017px"><use href="#icon-hand-heart"/></svg>
  <svg class="abs badge-icon" style="left:247px;top:1017px"><use href="#icon-handshake"/></svg>
  <div class="abs badge-label centered" style="left:175px;top:1045px">HAND CRAFTED</div>
  <div class="abs badge-label centered" style="left:247px;top:1045px">FAIR TRADE</div>

  <div class="abs maker" style="left:137px;top:1067px">
    MANUFACTURED BY:<br><strong>LINDENVALE PURE ORGANICS</strong><br>PO. BOX 4471 ELMRIDGE, VA 24019<br>themeadowlyco.com
  </div>

  <div class="abs photo-slot" style="left:477px;top:966px;width:85px;height:56px" role="img" aria-label="Engraved illustration of a cow standing in profile"></div>
  <div class="abs product-name centered" style="left:521px;top:1042px;font-size:22px;font-weight:400">TALLOW</div>
  <div class="abs product-name centered" style="left:521px;top:1069px;font-size:33px">FACE CREAM</div>
  <div class="abs" style="left:512px;top:1093px;width:17px;height:2px;background:var(--ink)"></div>
  <div class="abs net-weight centered" style="left:522px;top:1112px">NET WT.&nbsp; 4 OZ / 250G</div>

  <div class="abs ingredients" style="left:696px;top:941px;width:209px;font-size:13.4px;line-height:17.6px">
    <strong>Ingredients:</strong> Lorem ipsum dolor sit amet, consectetuer adipiscing elit, sed diam nonummy nibh euismod tincidunt ut laoreet dolore magna aliquam erat volutpat. Ut wisi enim ad minim veniam, quis nostrud exerci tation ullamcorper suscipit lobortis nisl ut aliquip ex ea commodo consequat. Duis autem vel eum iriure dolor in hendrerit in
  </div>
</section>

</body>
</html>
```